Female Focused - Finance Company needs a website

I need a website for a new company based in London called 'Lorinda Pelham Associates'. The company has been set up with a focus on empowering creativity and encouraging women to engage with finance and build their knowledge and understanding. I am targeting professional women and entrepreneurs in the late 20s to 40s age bracket. The mission is to empower women to achieve financial independence and inspire community and connectivity. I want to create a brand that promotes financial security, growth and connectivity.

The website at this stage can be relatively simple, I just want to be able to have a section about me and the work that I do, have contact details for people to be able to get in touch and find out more.

I run a series of different events and want to have a page whereby I can showcase the events that I am running. They can also use links to click through and register for events. I also want to be able to put images up of previous events that I have run. Maybe having a calendar on the website of different things that are happening.

I am creating a membership club called Hop3Hop and I want to have a page whereby they can find out about the membership and the different options that are available.

I have attached the logo below so you can see the designs so far.

I also own the domain name lorindapelhamassociates.com

```html
<!DOCTYPE html>
<html lang="en">
<head>
<meta charset="utf-8">
<title>Lorinda Pelham Associates</title>
<link href="https://fonts.googleapis.com/css2?family=Playfair+Display:wght@400;500;700&family=Roboto:wght@400;500;700&display=swap" rel="stylesheet">
<style>
:root{
  --violet:#7b74c9;
  --violet-dark:#6a63b8;
  --ink:#1f1d3a;
  --text:#4a4860;
  --lavender:#eceaf6;
  --hero-bg:#e8e6f4;
  --navy:#2e2c57;
  --white:#ffffff;
}
*{box-sizing:border-box;margin:0;padding:0}
html,body{width:1200px;height:4444px;overflow:hidden}
body{font-family:'Roboto',sans-serif;color:var(--text);background:var(--white);position:relative}
.serif{font-family:'Playfair Display',serif}
section,header,footer{position:absolute;left:0;width:1200px}
.abs{position:absolute}
.label{font-size:12px;letter-spacing:1.6px;font-weight:500;color:#5b5870;text-transform:uppercase}
.h2{font-family:'Playfair Display',serif;font-size:29px;color:var(--ink);font-weight:400;line-height:1.3}
.body-text{font-size:13px;line-height:25px;color:var(--text)}
.btn{position:absolute;background:var(--violet);color:#fff;font-size:13px;display:flex;align-items:center;justify-content:center;gap:10px;border-radius:2px}
.photo{position:absolute}
.brand-name{font-family:'Playfair Display',serif;color:var(--ink);font-weight:400;text-align:center}

/* hero */
.hero{top:0;height:714px;background:radial-gradient(circle at 72% 30%,#f4dbe8 0,#ebe4f3 28%,var(--hero-bg) 60%)}
.logo{left:100px;top:28px;width:130px;text-align:center}
.logo .ring{width:64px;height:64px;border:1.5px solid var(--ink);border-radius:50%;margin:0 auto 6px}
.logo .brand-name{font-size:11px;line-height:14px}
.nav{top:60px;left:515px;display:flex;gap:44px;font-family:'Playfair Display',serif;font-size:12.5px;letter-spacing:.6px;color:var(--ink)}
.hero h1{left:100px;top:212px;width:640px;font-family:'Playfair Display',serif;font-weight:400;font-size:40px;line-height:48px;color:var(--ink)}
.hero .body-text{left:100px;top:386px;width:540px}
.call{left:305px;top:506px;display:flex;align-items:center;gap:14px}
.call .ic{width:42px;height:42px;border-radius:50%;background:#fff;display:flex;align-items:center;justify-content:center}
.call small{font-size:11.5px;color:#77748a;display:block}
.call strong{font-size:18px;color:var(--ink);font-weight:500}

/* about */
.about{top:714px;height:678px}
.about .h2{font-size:28px}

/* events */
.events{top:1392px;height:630px;background:var(--lavender)}
.center{text-align:center;width:100%}
.card{position:absolute;background:#fff;box-shadow:0 6px 18px rgba(60,55,120,.07)}
.card .img{height:172px}
.card .date{font-size:12.5px;color:var(--violet);font-weight:500;padding:14px 14px 0;display:flex;align-items:center;gap:8px}
.card .title{font-family:'Playfair Display',serif;font-size:14.5px;line-height:25px;color:var(--ink);padding:8px 14px 0}

/* gallery */
.gallery{top:2022px;height:626px}
.tile{position:absolute;overflow:hidden}
.tile .cap{position:absolute;left:24px;right:24px;bottom:24px;color:#fff}
.tile .cap h4{font-family:'Playfair Display',serif;font-weight:500;line-height:1.35}
.tile .cap p{font-size:12.5px;color:#b7b2f0;margin-top:8px}
.tile .arrow{position:absolute;right:22px;bottom:26px}

/* membership */
.member{top:2648px;height:405px;background:var(--violet);overflow:hidden}
.member .label{color:#dcd9f6}
.member h2{font-family:'Playfair Display',serif;font-size:62px;font-weight:700;color:#fff;line-height:1}
.member .body-text{color:#eceaff}

/* blogs */
.blogs{top:3053px;height:594px;background:#f9f9fc}
.blog .date{font-size:12.5px;color:var(--violet);font-weight:500;padding:16px 20px 0}
.blog .title{font-family:'Playfair Display',serif;font-size:14.5px;line-height:25px;color:var(--ink);padding:6px 20px 0}
.circle-btn{position:absolute;width:28px;height:28px;border-radius:50%;background:var(--violet);display:flex;align-items:center;justify-content:center}

/* contact */
.contact{top:3647px;height:466px;background:#fff}
.contact .info{font-size:13px;line-height:20px;color:#2a2840}
.contact .accent{color:var(--violet)}
.social{position:absolute;width:28px;height:28px;border-radius:50%;background:var(--violet)}
.form{position:absolute;left:557px;top:41px;width:536px;height:395px;background:#fff;box-shadow:0 8px 30px rgba(60,55,120,.12)}
.field{position:absolute;border:1px solid #cfcde0;font-size:11px;color:#6d6a80;padding:12px 14px}

/* footer */
.footer{top:4113px;height:331px;background:var(--navy);color:#e6e4f7}
.footer .nav-foot{top:180px;left:0;width:1200px;display:flex;justify-content:center;gap:0;font-size:13px}
.footer .nav-foot span{width:98px;text-align:center}
</style>
</head>
<body>

<header class="hero">
  <div class="abs logo">
    <div class="ring"></div>
    <div class="brand-name">Lorinda Pelham<br>Associates</div>
    <div style="font-size:6px;letter-spacing:1.5px;margin-top:4px;color:#777">EMPOWERING CREATIVITY</div>
  </div>
  <nav class="abs nav">
    <span>HOME</span><span>ABOUT ME</span><span>EVENTS</span><span>NEWS</span><span>MEMBERSHIP</span><span>CONTACT</span>
  </nav>
  <h1 class="abs">We`re Empowering Creativity &amp; Encouraging to Engage with Finance</h1>
  <p class="abs body-text">Lorem Ipsum is simply dummy text of the printing and typesetting industry. Lorem Ipsum has been the industry's standard dummy text ever since the 1500s, when an unknown printer took a galley of type and scrambled it to make a type specimen book.</p>
  <div class="btn" style="left:100px;top:508px;width:177px;height:44px">Make an appointment</div>
  <div class="abs call">
    <div class="ic"><svg width="18" height="18" viewBox="0 0 24 24" fill="none" stroke="#7b74c9" stroke-width="2"><path d="M22 16.9v3a2 2 0 0 1-2.2 2 19.8 19.8 0 0 1-8.6-3.1 19.5 19.5 0 0 1-6-6A19.8 19.8 0 0 1 2.1 4.2 2 2 0 0 1 4.1 2h3a2 2 0 0 1 2 1.7c.1 1 .4 1.9.7 2.8a2 2 0 0 1-.5 2.1L8 9.9a16 16 0 0 0 6 6l1.3-1.3a2 2 0 0 1 2.1-.4c.9.3 1.8.6 2.8.7a2 2 0 0 1 1.7 2z"/></svg></div>
    <div><small>Call Now</small><strong>+44 20 7946 0380</strong></div>
  </div>
  <div class="photo" role="img" aria-label="Portrait of a smiling businesswoman in a black blazer" style="left:720px;top:150px;width:280px;height:564px;background:linear-gradient(180deg,#3a3035 0%,#1e1c22 60%,#2a2730 100%);border-radius:140px 140px 0 0"></div>
</header>

<section class="about">
  <div class="photo" role="img" aria-label="Portrait of a smiling blonde woman with glasses, arms crossed" style="left:103px;top:83px;width:427px;height:490px;background:linear-gradient(160deg,#e6e5e3,#cfcbc6 55%,#2b2a2e 56%,#1d1c20)"></div>
  <div class="abs label" style="left:600px;top:116px">About Me</div>
  <div class="abs" style="left:692px;top:123px;width:78px;height:1px;background:#b9b6cf"></div>
  <h2 class="abs h2" style="left:600px;top:146px;width:480px">Feel Confident in you financial future with me</h2>
  <p class="abs body-text" style="left:600px;top:248px;width:490px">Lorem Ipsum is simply dummy text of the printing and typesetting industry. Lorem Ipsum has been the industry's standard dummy text ever since the 1500s, when an unknown printer took a galley of type and scrambled it to make a type specimen book. Lorem Ipsum is simply dummy text of the printing and typesetting industry.</p>
  <p class="abs body-text" style="left:600px;top:398px;width:490px">Lorem Ipsum has been the industry's standard dummy text ever since the 1500s, when an unknown printer took a galley of type and scrambled it to make a type specimen book.</p>
  <div class="btn" style="left:600px;top:496px;width:195px;height:45px">Learn more about me
    <svg width="16" height="10" viewBox="0 0 16 10" fill="none" stroke="#fff" stroke-width="1.5"><path d="M0 5h15M11 1l4 4-4 4"/></svg></div>
</section>

<section class="events">
  <div class="abs label center" style="top:70px">Upcoming Events</div>
  <h2 class="abs h2 center" style="top:100px">Attend a Lorinda Pelham Event Today</h2>
  <p class="abs body-text center" style="top:152px;left:350px;width:500px">Lorem Ipsum has been the industry's standard dummy text ever since the 1500s, when an unknown printer took a galley of type and scrambled it to make a type specimen book.</p>

  <div class="card" style="left:100px;top:259px;width:314px;height:306px">
    <div class="img" role="img" aria-label="Women laughing together around a laptop at a table" style="background:linear-gradient(135deg,#cdb9a4,#8a7565 60%,#e8e2da)"></div>
    <div class="date"><svg width="18" height="16" viewBox="0 0 18 16" fill="none" stroke="#7b74c9"><rect x=".5" y="2" width="17" height="13.5"/><path d="M.5 6h17M4 0v3M14 0v3"/></svg>JANUARY 24 2023 @ 10:00AM - 12:00PM</div>
    <div class="title">Lorem Ipsum is simply dummy text of the printing and typesetting industry</div>
  </div>
  <div class="card" style="left:443px;top:259px;width:314px;height:306px">
    <div class="img" role="img" aria-label="Speaker at a microphone facing a seated audience" style="background:linear-gradient(135deg,#6d7d92,#2d3a4b 55%,#515d6d)"></div>
    <div class="date"><svg width="18" height="16" viewBox="0 0 18 16" fill="none" stroke="#7b74c9"><rect x=".5" y="2" width="17" height="13.5"/><path d="M.5 6h17M4 0v3M14 0v3"/></svg>JANUARY 24 2023 @ 10:00AM - 12:00PM</div>
    <div class="title">Lorem Ipsum is simply dummy text of the printing and typesetting industry</div>
  </div>
  <div class="card" style="left:785px;top:259px;width:314px;height:306px">
    <div class="img" role="img" aria-label="Presenter at a laptop in front of a large audience" style="background:linear-gradient(135deg,#b24e33,#de9a6e 45%,#3b2a27)"></div>
    <div class="date"><svg width="18" height="16" viewBox="0 0 18 16" fill="none" stroke="#7b74c9"><rect x=".5" y="2" width="17" height="13.5"/><path d="M.5 6h17M4 0v3M14 0v3"/></svg>JANUARY 24 2023 @ 10:00AM - 12:00PM</div>
    <div class="title">Lorem Ipsum is simply dummy text of the printing and typesetting industry</div>
  </div>
</section>

<section class="gallery">
  <div class="abs label" style="left:100px;top:56px">Event Gallery</div>
  <h2 class="abs h2" style="left:98px;top:80px">Past Event Showcase</h2>
  <div class="btn" style="left:910px;top:70px;width:190px;height:43px">More events images
    <svg width="16" height="10" viewBox="0 0 16 10" fill="none" stroke="#fff" stroke-width="1.5"><path d="M0 5h15M11 1l4 4-4 4"/></svg></div>

  <div class="tile" role="img" aria-label="Woman speaking into a microphone on a dark stage before a crowd" style="left:100px;top:140px;width:640px;height:400px;background:linear-gradient(160deg,#3b3a3e,#1b1a1d 50%,#3a2a20)">
    <div class="cap"><h4 style="font-size:19px;width:420px">Lorem Ipsum is simply dummy text of the printing and typesetting industry</h4><p>Event locaiton | &nbsp;Jan 10 2023</p></div>
    <svg class="arrow" width="16" height="12" viewBox="0 0 16 12" fill="none" stroke="#fff" stroke-width="1.5"><path d="M0 6h15M10 1l5 5-5 5"/></svg>
  </div>
  <div class="tile" role="img" aria-label="Speaker facing a full conference hall" style="left:752px;top:140px;width:348px;height:231px;background:linear-gradient(180deg,#d9d6d3,#6a4d49 55%,#2a2224)">
    <div class="cap" style="bottom:20px"><h4 style="font-size:14.5px">Lorem Ipsum is simply dummy text of the printing and typesetting industry</h4><p>Event locaiton | &nbsp;Jan 10 2023</p></div>
    <svg class="arrow" style="bottom:20px" width="16" height="12" viewBox="0 0 16 12" fill="none" stroke="#fff" stroke-width="1.5"><path d="M0 6h15M10 1l5 5-5 5"/></svg>
  </div>
  <div class="tile" role="img" aria-label="Audience in a dim hall under stage lights" style="left:752px;top:381px;width:348px;height:159px;background:linear-gradient(180deg,#4a3f6a,#2a2238 60%,#1c1822)">
    <div class="cap" style="bottom:20px"><h4 style="font-size:14.5px">Lorem Ipsum is simply dummy text of the printing and typesetting industry</h4><p>Event locaiton | &nbsp;Jan 10 2023</p></div>
    <svg class="arrow" style="bottom:20px" width="16" height="12" viewBox="0 0 16 12" fill="none" stroke="#fff" stroke-width="1.5"><path d="M0 6h15M10 1l5 5-5 5"/></svg>
  </div>
</section>

<section class="member">
  <svg class="abs" style="left:735px;top:0" width="330" height="405" viewBox="0 0 330 405" fill="none" stroke="#5f58a8" stroke-width="1.5">
    <path d="M0 0v250a165 165 0 0 0 330 0V0"/>
    <path d="M18 0v240a147 147 0 0 0 294 0V0"/>
    <path d="M36 0v230a129 129 0 0 0 258 0V0"/>
  </svg>
  <div class="abs" style="left:764px;top:52px;width:272px;height:272px;border-radius:50%;background:#fff;display:flex;align-items:center;justify-content:center">
    <div class="brand-name" style="font-size:24px;line-height:1.3">Lorinda Pelham<br>Associates</div>
  </div>
  <div class="abs label" style="left:108px;top:54px">Membership Program</div>
  <h2 class="abs" style="left:107px;top:80px">Hop3Hop</h2>
  <p class="abs body-text" style="left:108px;top:166px;width:490px">Lorem Ipsum is simply dummy text of the printing and typesetting industry. Lorem Ipsum has been the industry's standard dummy text ever since the 1500s, when an unknown printer took a galley of type and scrambled it to make a type specimen book. Lorem Ipsum is simply dummy text of the printing and typesetting industry.</p>
  <div class="btn" style="left:108px;top:315px;width:218px;height:44px;background:var(--navy)">Click here for Membership
    <svg width="16" height="10" viewBox="0 0 16 10" fill="none" stroke="#fff" stroke-width="1.5"><path d="M0 5h15M11 1l4 4-4 4"/></svg></div>
</section>

<section class="blogs">
  <div class="abs label center" style="top:79px">Latest Blogs</div>
  <h2 class="abs h2 center" style="top:108px;font-size:30px">Take a look at the latest articles from Lorinda Pelham</h2>

  <div class="card blog" style="left:103px;top:179px;width:314px;height:308px">
    <div class="img" role="img" aria-label="Speaker on stage addressing a banquet audience" style="background:linear-gradient(160deg,#3a5a9a,#1b2233 55%,#5b3a2c)"></div>
    <div class="circle-btn" style="left:272px;top:136px"><svg width="12" height="10" viewBox="0 0 12 10" fill="none" stroke="#fff" stroke-width="1.5"><path d="M0 5h11M7 1l4 4-4 4"/></svg></div>
    <div class="date">JANUARY 24 2023</div>
    <div class="title">Lorem Ipsum is simply dummy text of the printing and typesetting industry. Lorem Ipsum has been the industry's</div>
  </div>
  <div class="card blog" style="left:445px;top:179px;width:315px;height:308px">
    <div class="img" role="img" aria-label="Crowd of women at a networking event" style="background:linear-gradient(160deg,#c9b08e,#6a4e3a 55%,#a88466)"></div>
    <div class="circle-btn" style="left:273px;top:136px"><svg width="12" height="10" viewBox="0 0 12 10" fill="none" stroke="#fff" stroke-width="1.5"><path d="M0 5h11M7 1l4 4-4 4"/></svg></div>
    <div class="date">JANUARY 24 2023</div>
    <div class="title">Lorem Ipsum is simply dummy text of the printing and typesetting industry. Lorem Ipsum has been the industry's</div>
  </div>
  <div class="card blog" style="left:788px;top:179px;width:315px;height:308px">
    <div class="img" role="img" aria-label="Colleagues in colourful clothing meeting in an office" style="background:linear-gradient(135deg,#e9e4de,#e08a4a 45%,#3a4a6a)"></div>
    <div class="circle-btn" style="left:273px;top:136px"><svg width="12" height="10" viewBox="0 0 12 10" fill="none" stroke="#fff" stroke-width="1.5"><path d="M0 5h11M7 1l4 4-4 4"/></svg></div>
    <div class="date">JANUARY 24 2023</div>
    <div class="title">Lorem Ipsum is simply dummy text of the printing and typesetting industry. Lorem Ipsum has been the industry's</div>
  </div>

  <div class="circle-btn" style="left:563px;top:516px"><svg width="12" height="10" viewBox="0 0 12 10" fill="none" stroke="#fff" stroke-width="1.5"><path d="M12 5H1M5 1L1 5l4 4"/></svg></div>
  <div class="circle-btn" style="left:608px;top:516px"><svg width="12" height="10" viewBox="0 0 12 10" fill="none" stroke="#fff" stroke-width="1.5"><path d="M0 5h11M7 1l4 4-4 4"/></svg></div>
</section>

<section class="contact">
  <div class="abs" style="left:100px;top:44px;display:flex;align-items:center;gap:10px">
    <div style="width:56px;height:56px;border:1.5px solid var(--ink);border-radius:50%"></div>
    <div class="brand-name" style="font-size:12px;text-align:left;line-height:15px">Lorinda Pelham<br>Associates</div>
  </div>
  <h2 class="abs h2" style="left:100px;top:132px">Contact Me Today</h2>
  <p class="abs info" style="left:98px;top:180px">48 Harrow Lane #2, Camden,<br>London NW1 7QB, UK</p>
  <p class="abs info" style="left:98px;top:238px"><span class="accent" style="font-size:12px">QUESTIONS?</span><br>Phone: 020-7946-0381<br>Fax: 020-7946-0382</p>
  <p class="abs info" style="left:98px;top:330px">Email : <span class="accent">info@lorindapelhamassociates.com</span></p>
  <div class="social" role="img" aria-label="Social link" style="left:102px;top:380px"></div>
  <div class="social" role="img" aria-label="Social link" style="left:148px;top:380px"></div>
  <div class="social" role="img" aria-label="Social link" style="left:194px;top:380px"></div>
  <div class="social" role="img" aria-label="Social link" style="left:241px;top:380px"></div>

  <div class="form">
    <div class="abs center" style="top:46px;font-size:15px;font-weight:500;color:#2a2840">Please fill out theform below to contact us</div>
    <div class="field" style="left:52px;top:94px;width:207px;height:42px">Name</div>
    <div class="field" style="left:276px;top:94px;width:207px;height:42px">Email</div>
    <div class="field" style="left:52px;top:156px;width:431px;height:135px">Message</div>
    <div class="btn" style="left:188px;top:308px;width:167px;height:42px;font-weight:500;letter-spacing:.5px">CONTACT NOW</div>
  </div>
</section>

<footer class="footer">
  <div class="abs" style="left:555px;top:52px;width:90px;height:90px;border:1.5px solid #c9c6ee;border-radius:50%;display:flex;align-items:center;justify-content:center">
    <div class="brand-name" style="color:#e6e4f7;font-size:11px;line-height:14px">Lorinda<br>Pelham<br>Associates</div>
  </div>
  <nav class="abs nav-foot"><span>Home</span><span>About me</span><span>Events</span><span>News</span><span>Membership</span><span>Contact</span></nav>
  <div class="abs" style="left:100px;top:222px;width:1000px;height:1px;background:#4a477a"></div>
  <div class="abs center" style="top:242px;font-size:9.5px">Privacy Policy | Terms of use</div>
  <div class="abs center" style="top:268px;font-size:11.5px">Copyright ©2023 lorindapelhamassociates.com</div>
</footer>

</body>
</html>
```